Larkspur Ridge Management - Business Cards

I need business cards. My current logo was designed by a designer at this site and I very much like and am happy with the results. I would like a business card that is trendy, unique, current yet professional. I deal with high net worth clients daily

Target Market(s)

Out of state investors looking to get into the rental market in Ohio

Industry/Entity Type

Property Management, Consulting

Contact Information for Business Card

Name, Title (Chief Financial Officer) office phone number (555) 817-3094 website address larkridgemgmt.example

Font styles to use
Sans Serif

Colors
0054AA
0677BA
7BADD7
CADEEF
E8F1F8
0094D4
00A9DD
6FCCEA
C7EBF8
E9F6FB
00AB8E
00BBA5
67D7C9
C6EFE9
E9F9F6

```html
<!DOCTYPE html>
<html lang="en">
<head>
<meta charset="utf-8">
<title>Larkspur Ridge Management – Business Cards</title>
<link rel="stylesheet" href="https://fonts.googleapis.com/css2?family=Lato:wght@400;700;900&display=swap">
<style>
  :root {
    --navy: #22325a;
    --red: #cc2a31;
    --white: #ffffff;
    --ink: #3a3a3a;
    --teal: #0aad8f;
    --backdrop: #1c1c1c;
  }
  * { margin: 0; padding: 0; box-sizing: border-box; }
  html, body { width: 1200px; height: 1059px; overflow: hidden; }
  body {
    background: var(--backdrop);
    font-family: "Lato", sans-serif;
    position: relative;
  }
  .card {
    position: absolute;
    left: 260px;
    border-radius: 26px;
    overflow: hidden;
  }
  .card-front { top: 94px; width: 709px; height: 405px; background: var(--white); }
  .card-back { top: 572px; width: 702px; height: 400px; background: var(--teal); }

  .front-waves { position: absolute; inset: 0; width: 709px; height: 405px; }

  .brand-name {
    position: absolute;
    font-weight: 900;
    color: var(--navy);
    text-align: center;
    line-height: 1.05;
    text-transform: uppercase;
  }
  .card-front .brand-name { left: 28px; top: 88px; width: 240px; font-size: 29px; }
  .card-back .brand-name { left: 0; top: 148px; width: 702px; font-size: 44px; }

  .holder { position: absolute; right: 77px; top: 46px; text-align: right; }
  .holder-name { font-size: 29px; font-weight: 700; color: var(--navy); letter-spacing: -0.2px; line-height: 1; }
  .holder-title { font-size: 19px; font-weight: 400; color: var(--ink); margin-top: 10px; line-height: 1; }
  .accent-bar { position: absolute; right: 0; top: 45px; width: 14px; height: 60px; background: var(--red); }

  .contact-list { position: absolute; right: 44px; top: 230px; list-style: none; }
  .contact-item {
    display: flex; align-items: center; justify-content: flex-end;
    height: 31.5px; font-size: 18.5px; color: var(--white);
  }
  .contact-item svg { width: 20px; height: 20px; margin-left: 24px; flex: none; }
  .address {
    position: absolute; right: 43px; top: 328px; text-align: right;
    font-size: 18.5px; line-height: 27px; color: var(--white); font-style: normal;
  }
</style>
</head>
<body>

<section class="card card-front">
  <svg class="front-waves" viewBox="0 0 1206 688" preserveAspectRatio="none" aria-hidden="true">
    <path fill="var(--red)" d="M0,458 C120,505 220,510 300,505 C420,495 500,445 565,395 C480,470 380,545 258,550 C150,552 70,530 0,508 Z"/>
    <path fill="var(--navy)" d="M0,528 C180,590 360,585 540,490 C740,380 880,290 1065,277 C1100,282 1150,310 1206,335 L1206,688 L0,688 Z"/>
    <path fill="none" stroke="var(--white)" stroke-width="14" d="M143,608 C330,660 520,560 700,450 C850,360 980,300 1206,330"/>
  </svg>

  <div class="brand-name">Larkspur Ridge Management</div>

  <div class="holder">
    <div class="holder-name">DANIEL WHITFORD</div>
    <div class="holder-title">Chief Financial Officer</div>
  </div>
  <div class="accent-bar"></div>

  <ul class="contact-list">
    <li class="contact-item">(555) 817-3094
      <svg viewBox="0 0 24 24"><path fill="var(--red)" d="M6.6 10.8a15.1 15.1 0 0 0 6.6 6.6l2.2-2.2c.3-.3.7-.4 1-.2 1.1.4 2.3.6 3.6.6.6 0 1 .4 1 1V20c0 .6-.4 1-1 1A17 17 0 0 1 3 4c0-.6.4-1 1-1h3.5c.6 0 1 .4 1 1 0 1.3.2 2.5.6 3.6.1.3 0 .7-.2 1z"/></svg>
    </li>
    <li class="contact-item">info@larkridge.example
      <svg viewBox="0 0 24 24"><path fill="var(--red)" d="M2 5h20v2l-10 6L2 7z"/><path fill="var(--red)" d="M2 9l10 6 10-6v10H2z"/></svg>
    </li>
    <li class="contact-item">www.larkridgemgmt.example
      <svg viewBox="0 0 24 24" fill="none" stroke="var(--red)" stroke-width="2"><circle cx="12" cy="12" r="9.5"/><ellipse cx="12" cy="12" rx="4" ry="9.5"/><path d="M2.5 12h19M4 7h16M4 17h16"/></svg>
    </li>
  </ul>
  <address class="address">421, Address line goes here<br>45452, Country name</address>
</section>

<section class="card card-back">
  <div class="brand-name">Larkspur Ridge<br>Management</div>
</section>

</body>
</html>
```